Vegan Alfredo Sauce Label Design for Brambleway Pantry Co

We are a food co. committed to making vegan food more accessible to people who want to eat healthier. Our first line of product is vegan Alfredo sauce.
We have 3 flavors:
- Garlic
- Pesto
- Lemony Artichoke
The current project is the design for the first flavor: garlic. However, we would like a template that would translate well to other flavors, so they look like a family of products.
These will be in standard 16 oz jars. The whole label will be approx 6cm x 24cm, but the front visual space is approx 6cm x 10cm. The rest will be nutritional labeling and copy about the company.
We also need a stamp or font- based logo that says Brambleway Pantry Co. (or lower case: brambleway pantry co.), the name of the company.
The picture (attached) of Plantbased Nacho Dip is the closest to what we are going for. Because the sauce is creamy white, a colorful background with off-white font will be best.
We currently have a website, although we are doing a brand over-haul (hence, this posting) www.bramblewaypantryco.example. If the designer is a good fit, we have several more projects, in line.
Other brands we love: Tidewell Grocers, Marlow Ridge Provisions, Pulp Poured Daily.
The final brand should communicate hip, natural and health.
And personally, I love design that is clever and somehow makes me smile.
Target Market(s)
Vegans, vegetarians, and people with common food allergies - all ages.
Young, hip families.
Industry/Entity Type
It Company
Requirements
Must have
- Copy:
Vegan Alfredo or Vegan Alfredo Sauce
Garlic
Brambleway Pantry or Brambleway Pantry Co
16 oz
Nice to have
- May include copy:
Gluten-Free Soy-Free Nut-Free
Should not have
- Neon colors

```html
<!DOCTYPE html>
<html lang="en">
<head>
<meta charset="utf-8">
<title>Brambleway Pantry Co. — Vegan Alfredo Sauce, Garlic</title>
<link rel="stylesheet" href="https://fonts.googleapis.com/css2?family=EB+Garamond:wght@400&family=Oswald:wght@400;500&display=swap">
<style>
  :root {
    --page: #ffffff;
    --label-green: #068553;
    --sketch-green: #3aa670;
    --cream: #f5f0d3;
    --ink-green: #068553;
    --night: #000000;
    --garlic-orange: #e8801e;
    --brand-text: #f5f0d3;
  }
  html, body {
    margin: 0;
    padding: 0;
    width: 1200px;
    height: 1000px;
    overflow: hidden;
    background: var(--page);
  }
  .canvas {
    position: relative;
    width: 1200px;
    height: 1000px;
  }
  .label {
    position: absolute;
    left: 96px;
    top: 224px;
    width: 1008px;
    height: 566px;
    background: var(--label-green);
    overflow: hidden;
  }
  .label-texture {
    position: absolute;
    inset: 0;
    background:
      radial-gradient(ellipse 260px 230px at 190px 250px, rgba(58,166,112,0.35), transparent 70%),
      radial-gradient(ellipse 240px 200px at 860px 110px, rgba(58,166,112,0.35), transparent 70%),
      radial-gradient(ellipse 230px 220px at 860px 440px, rgba(58,166,112,0.35), transparent 70%);
  }
  .brand-name {
    position: absolute;
    left: 0;
    width: 1008px;
    top: 130px;
    margin: 0;
    text-align: center;
    font-family: "EB Garamond", Georgia, serif;
    font-weight: 400;
    font-size: 22px;
    letter-spacing: 0.2px;
    color: var(--brand-text);
  }
  .product-panel {
    position: absolute;
    left: 394px;
    top: 179px;
    width: 193px;
    height: 387px;
    background: var(--cream);
  }
  .product-title {
    margin: 0;
    padding-top: 28px;
    text-align: center;
    font-family: "Oswald", "Arial Narrow", sans-serif;
    font-weight: 500;
    font-size: 29px;
    line-height: 44px;
    letter-spacing: 0.5px;
    color: var(--ink-green);
  }
  .flavor-box {
    position: absolute;
    left: 355px;
    top: 347px;
    width: 275px;
    height: 179px;
    background: var(--night);
  }
  .flavor-art {
    position: absolute;
    left: 88px;
    top: 20px;
    width: 100px;
    height: 105px;
    background: radial-gradient(ellipse at 50% 60%, rgba(245,240,211,0.35), rgba(245,240,211,0.05) 70%, transparent);
  }
  .flavor-name {
    position: absolute;
    left: 0;
    width: 275px;
    top: 138px;
    margin: 0;
    text-align: center;
    font-family: "Oswald", "Arial Narrow", sans-serif;
    font-weight: 500;
    font-size: 21px;
    color: var(--garlic-orange);
  }
  .product-facts {
    position: absolute;
    left: 394px;
    top: 538px;
    width: 193px;
    margin: 0;
    text-align: center;
    font-family: "Oswald", "Arial Narrow", sans-serif;
    font-weight: 400;
    font-size: 13px;
    color: var(--ink-green);
    white-space: nowrap;
  }
  .product-facts .net-weight {
    margin-left: 12px;
  }
</style>
</head>
<body>
  <div class="canvas">
    <section class="label">
      <div class="label-texture" role="img" aria-label="Loose hand-drawn sketch of garlic bulbs and stems in lighter green across the background"></div>

      <p class="brand-name">Brambleway Pantry Co.</p>

      <div class="product-panel">
        <h1 class="product-title">VEGAN<br>ALFREDO<br>SAUCE</h1>
      </div>

      <div class="flavor-box">
        <div class="flavor-art" role="img" aria-label="Cream line drawing of a garlic bulb"></div>
        <p class="flavor-name">GARLIC</p>
      </div>

      <p class="product-facts">Gluten/Soy/Nut Free <span class="net-weight">16 oz.</span></p>
    </section>
  </div>
</body>
</html>
```